Serlivo Business Cards

We need new Business Cards for our startup. It just launched.It is working in the high-end it-market. Specifically in the cloud area. We are a hybrid cloud company. The company logo is attached. We are a Swiss based company. Information visible on the card is: 1. Logo 2. Company Name: Serlivo AG 3. Subtitle: Hybrid Clouds. 3. Name: Tobias Ferrand 4. Adress: Lindenhofweg 14a, 8457 Albrunn, Switzerland 5. Email: tobias@serlivo-mail.ch. 6. Mobile: +41 79 386 42 15. It should be a grey/white design. Similar to the attached logo. It should have class, high-quality but not too much color and no gold used.
Updates

I forgot to add my Position. Please use Founder / CEO. thanks tobias

Industry/Entity Type

Business

```html
<!DOCTYPE html>
<html lang="en">
<head>
<meta charset="utf-8">
<title>Serlivo AG – Business Cards</title>
<link rel="stylesheet" href="https://fonts.googleapis.com/css2?family=Open+Sans:wght@300;400;600&display=swap">
<style>
  :root {
    --backdrop: #e6e6e6;
    --card-grey: #a4a4a4;
    --card-white: #f4f4f2;
    --ink-light: #f2f2f2;
    --ink-soft: #e4e4e4;
    --ink-grey: #9a9a9a;
    --shadow: rgba(0, 0, 0, 0.18);
  }
  * { margin: 0; padding: 0; box-sizing: border-box; }
  html, body {
    width: 1200px;
    height: 1000px;
    overflow: hidden;
    background: var(--backdrop);
    font-family: "Open Sans", sans-serif;
  }
  .sheet {
    position: relative;
    width: 1200px;
    height: 1000px;
  }
  .card {
    position: absolute;
    left: 275px;
    width: 650px;
    height: 420px;
    box-shadow: 0 6px 18px var(--shadow);
    overflow: hidden;
  }
  .card--front {
    top: 55px;
    background: var(--card-grey);
    display: flex;
    align-items: center;
    justify-content: center;
  }
  .card--back {
    top: 525px;
    display: flex;
  }
  .brand {
    display: flex;
    align-items: center;
    gap: 22px;
    font-weight: 300;
    letter-spacing: 0.42em;
    text-transform: uppercase;
  }
  .brand__dot {
    width: 40px;
    height: 40px;
    border-radius: 50%;
    border: 1.5px solid currentColor;
  }
  .card--front .brand {
    color: var(--ink-light);
    font-size: 40px;
  }
  .back__info {
    width: 50%;
    background: var(--card-grey);
    padding: 30px 0 0 46px;
    color: var(--ink-light);
  }
  .company {
    text-align: center;
    padding-right: 46px;
    margin-bottom: 46px;
  }
  .company__name {
    font-weight: 600;
    font-size: 24px;
    line-height: 1.2;
  }
  .company__tagline {
    font-size: 14px;
    color: var(--ink-soft);
  }
  .person__name {
    font-weight: 600;
    font-size: 21px;
    line-height: 1.25;
  }
  .person__role {
    font-size: 18px;
    margin-bottom: 10px;
  }
  .contact {
    list-style: none;
    font-size: 15px;
    line-height: 1.75;
    color: var(--ink-soft);
  }
  .back__logo {
    width: 50%;
    background: var(--card-white);
    display: flex;
    align-items: center;
    justify-content: center;
  }
  .back__logo .brand {
    color: var(--ink-grey);
    font-size: 26px;
    gap: 16px;
  }
  .back__logo .brand__dot {
    width: 28px;
    height: 28px;
  }
</style>
</head>
<body>
<main class="sheet">
  <section class="card card--front" aria-label="Card front">
    <div class="brand">
      <span class="brand__dot"></span>
      <span class="brand__name">Serlivo</span>
    </div>
  </section>

  <section class="card card--back" aria-label="Card back">
    <div class="back__info">
      <header class="company">
        <p class="company__name">Serlivo AG</p>
        <p class="company__tagline">Hybrid Clouds</p>
      </header>
      <p class="person__name">Tobias Ferrand</p>
      <p class="person__role">Founder / CEO</p>
      <ul class="contact">
        <li>Lindenhofweg 14a</li>
        <li>8457 Albrunn, Switzerland</li>
        <li>E : tobias@serlivo-mail.ch</li>
        <li>P : +41 79 386 42 15</li>
        <li>W : www.serlivo-web.ch</li>
      </ul>
    </div>
    <div class="back__logo">
      <div class="brand">
        <span class="brand__dot"></span>
        <span class="brand__name">Serlivo</span>
      </div>
    </div>
  </section>
</main>
</body>
</html>
```